Web Design for an Online Dating Web Site

We need an uncoded web design for a new online dating web site called zMatchy.net. Simplicity and boldness are the key factors in the successful design.
Please look at the requirements document attached for details.
Updates
Dear all,
Please AVOID USING A PICTURE OF A HAPPY COUPLE ON THE HOME PAGE of the site. We highly want to move away from this space as it makes our web site just like another dating web site.
We like something simple with web 2.0 look and feel. The examples in the Requirements Document are exactly the design we are after.
Regards
Tarn
Industry/Entity Type
Dating
Look and feel
Each slider illustrates characteristics of the customer's brand and the style your logo design should communicate.

```html
<!DOCTYPE html>
<html lang="en">
<head>
<meta charset="utf-8">
<title>zMatchy.net – Home</title>
<link href="https://fonts.googleapis.com/css2?family=Open+Sans:ital,wght@0,400;0,600;0,700;1,400;1,700&family=Arimo:wght@400;700&display=swap" rel="stylesheet">
<style>
:root{
  --pink:#e2197a;
  --pink-light:#f05a9c;
  --teal:#3fb8cf;
  --teal-text:#44a9bc;
  --lime-top:#b3d94a;
  --lime-mid:#e6f2bc;
  --olive:#5f604f;
  --olive-num:#8cb532;
  --orange-top:#ffc61f;
  --orange-bot:#f7a100;
  --ink:#222;
  --body:#555;
  --footer:#2c2c2c;
  --footer-field:#3b3b3b;
}
*{box-sizing:border-box;margin:0;padding:0}
html,body{width:1200px;height:1039px;overflow:hidden;background:#fff}
.page{position:relative;width:1490px;height:1290px;transform:scale(.80537);transform-origin:0 0;font-family:"Open Sans",sans-serif;color:var(--ink);overflow:hidden}
.abs{position:absolute}

/* header */
.header{position:absolute;left:0;top:0;width:1490px;height:100px;background:linear-gradient(#fff,#f1f1f1)}
.brand{position:absolute;left:178px;top:14px;display:flex;align-items:center;gap:10px;font-weight:700;font-size:50px;color:var(--pink);letter-spacing:-1px;line-height:1}
.brand-dot{width:22px;height:22px;border-radius:50%;background:var(--pink)}
.nav a{position:absolute;top:42px;font-size:19px;color:#333;text-decoration:none;font-family:"Arimo",sans-serif}
.nav a.current{text-decoration:underline}
.signup-tab{position:absolute;left:1118px;top:-116px;width:188px;height:188px;border-radius:50%;background:var(--teal);box-shadow:0 2px 3px rgba(0,0,0,.15)}
.signup-tab span{position:absolute;left:0;right:0;top:124px;text-align:center;color:#fff;font-weight:600;font-size:28px}

/* hero */
.hero{position:absolute;left:0;top:97px;width:1490px;height:437px;background:linear-gradient(var(--lime-top) 0%,var(--lime-mid) 50%,#d2e890 80%,var(--lime-top) 100%)}
.zig{position:absolute;left:0;width:1490px;height:8px;background:linear-gradient(135deg,#fafafa 25%,transparent 25%) -4px 0,linear-gradient(225deg,#fafafa 25%,transparent 25%) -4px 0;background-size:8px 8px}
.zig.top{top:0}
.zig.bottom{bottom:0;transform:rotate(180deg);background:linear-gradient(135deg,#fff 25%,transparent 25%) -4px 0,linear-gradient(225deg,#fff 25%,transparent 25%) -4px 0;background-size:8px 8px}
.hero h1{position:absolute;left:186px;top:18px;font-weight:400;font-size:54px;color:#fff}
.points li{position:absolute;left:188px;list-style:none;display:flex;align-items:center;gap:18px;font-size:28px;color:var(--ink)}
.num{width:34px;height:34px;border:3px solid var(--olive-num);border-radius:50%;font-size:18px;font-style:italic;color:var(--olive-num);display:flex;align-items:center;justify-content:center}
.points b{font-weight:600}
.video{position:absolute;left:843px;top:32px}
.video-label{position:absolute;left:868px;top:334px;font-size:33px;font-weight:600;color:#fff}
.arrow{position:absolute;top:117px;width:116px;height:116px;border-radius:50%;background:var(--pink)}
.arrow.prev{left:-42px}.arrow.next{left:1417px}
.arrow svg{position:absolute;top:48px}
.dots span{position:absolute;top:402px;width:16px;height:16px;border-radius:50%;border:2px solid #fff}
.dots .on{background:var(--pink);border-color:var(--pink)}

/* login */
.field{position:absolute;top:562px;width:230px;height:44px;border:3px solid #ccc;border-radius:12px;padding-left:18px;font-size:17px;color:#aaa;display:flex;align-items:center}
.btn-pink{position:absolute;left:686px;top:564px;width:100px;height:40px;background:linear-gradient(var(--pink-light),var(--pink));color:#fff;font-size:23px;display:flex;align-items:center;justify-content:center}
.or{position:absolute;left:816px;top:556px;font-size:42px;color:#222}
.social{position:absolute;top:564px;width:40px;height:40px;border-radius:6px;color:#fff;font-size:9px;font-weight:700;display:flex;align-items:center;justify-content:center;box-shadow:0 2px 2px rgba(0,0,0,.25)}
.btn-orange{position:absolute;background:linear-gradient(var(--orange-top),var(--orange-bot));color:#7a4a00;display:flex;align-items:center;justify-content:center;border-radius:3px}

/* articles */
.thumb{position:absolute;top:647px;width:326px;height:116px}
.article h2{position:absolute;top:772px;width:326px;font-weight:400;font-size:22px;color:var(--teal-text);padding-bottom:3px;border-bottom:1px solid #ddd}
.article p{position:absolute;top:819px;width:315px;font-family:"Arimo",sans-serif;font-size:11.5px;line-height:18px;color:var(--body)}

/* blog */
.blog h3{position:absolute;left:993px;top:640px;font-weight:400;font-size:24px;color:#333}
.heart{position:absolute;left:993px;width:72px;height:56px;border-radius:24px 24px 36px 36px}
.post-title{position:absolute;left:1085px;width:136px;font-size:16.5px;line-height:18px;color:#e6317c;border-bottom:1px dashed #ddd;padding-bottom:2px}
.post-date{position:absolute;left:1085px;width:135px;text-align:right;font-size:10px;font-style:italic;color:#333}
.more-posts{position:absolute;left:1106px;top:990px;font-size:12.5px;font-style:italic;font-weight:700;color:var(--teal-text)}

/* footer */
.footer{position:absolute;left:0;top:1025px;width:1490px;height:265px;background:linear-gradient(#2a2a2a,#343434);color:#fff;font-family:"Arimo",sans-serif}
.footer h4{position:absolute;top:20px;font-family:"Open Sans",sans-serif;font-weight:600;font-size:16px}
.links li{position:absolute;left:191px;list-style:none;font-size:13px}
.links li::before{content:"›";color:var(--teal);margin-right:7px}
.ffield{position:absolute;background:var(--footer-field);border-radius:6px;color:#888;font-size:12px;padding:12px 15px}
.send{position:absolute;left:598px;top:207px;width:122px;height:36px;border-radius:8px;background:linear-gradient(#4a4a4a,#2e2e2e);font-size:15px;display:flex;align-items:center;justify-content:center;box-shadow:0 1px 2px #000}
.chip{position:absolute;background:#fff;color:#333;border:1px solid #ccc;border-radius:3px;display:flex;align-items:center;justify-content:center}
</style>
</head>
<body>
<div class="page">

  <header class="header">
    <div class="brand">zmatchy<span class="brand-dot"></span></div>
    <nav class="nav">
      <a style="left:577px" href="#">Why</a>
      <a class="current" style="left:657px" href="#">How It Works</a>
      <a style="left:807px" href="#">Sign Up</a>
      <a style="left:915px" href="#">Our Blog</a>
    </nav>
    <div class="signup-tab"><span>SIGN UP</span></div>
  </header>

  <section class="hero">
    <div class="zig top"></div>
    <h1>Why we are better?</h1>
    <ul class="points">
      <li style="top:120px"><span class="num">1</span><span><b>Lorem Ipsum</b> is simply dummy text</span></li>
      <li style="top:191px"><span class="num">2</span><span>It is a long <b>established fact</b></span></li>
      <li style="top:258px"><span class="num">3</span><span><b>There</b> are many variations</span></li>
    </ul>
    <svg class="video" width="298" height="290" viewBox="0 0 298 290">
      <circle cx="148" cy="144" r="143" fill="none" stroke="var(--olive)" stroke-width="7"/>
      <polygon points="131,79 189,137 131,196" fill="var(--olive)"/>
    </svg>
    <div class="video-label">WATCH A VIDEO</div>
    <div class="arrow prev"><svg style="left:58px" width="14" height="20"><polyline points="11,2 3,10 11,18" fill="none" stroke="#7a2050" stroke-width="3"/></svg></div>
    <div class="arrow next"><svg style="left:38px" width="14" height="20"><polyline points="3,2 11,10 3,18" fill="none" stroke="#7a2050" stroke-width="3"/></svg></div>
    <div class="dots"><span class="on" style="left:642px"></span><span style="left:684px"></span><span style="left:726px"></span></div>
    <div class="zig bottom"></div>
  </section>

  <div class="field" style="left:179px">Username</div>
  <div class="field" style="left:430px">Password</div>
  <div class="btn-pink">Log in</div>
  <div class="or">Or</div>
  <div class="social" style="left:892px;background:#3d6bb0" aria-label="Friendly">Friendly</div>
  <div class="social" style="left:953px;background:#3eaac4" aria-label="Chirper">Chirper</div>
  <div class="social" style="left:1013px;background:#c8262b" aria-label="Vidwave">Vidwave</div>
  <div class="social" style="left:1074px;background:#3b78b5" aria-label="Searchly">Searchly</div>
  <div class="btn-orange" style="left:1156px;top:564px;width:100px;height:40px;font-size:18px">View more</div>

  <article class="article">
    <div class="thumb" style="left:177px;background:linear-gradient(#8a6a4a,#d9d3cc 55%,#b8b0a6)" role="img" aria-label="Bubble bath with champagne and glasses"></div>
    <h2 style="left:177px">Contrary to popular belief</h2>
    <p style="left:179px">But I must explain to you how all this mistaken idea of denouncing pleasure and praising pain was born and I will give you a complete account of the system, and expound the actual teachings of the great explorer of the truth, the master-builder of human happiness. No one rejects, dislikes, or avoids pleasure itself</p>
    <div class="btn-orange" style="left:176px;top:944px;width:144px;height:44px;font-size:20px">Read more</div>
  </article>
  <article class="article">
    <div class="thumb" style="left:563px;background:linear-gradient(90deg,#d97a62,#e8977e 60%,#8a5a4a)" role="img" aria-label="Close-up skin tones photograph"></div>
    <h2 style="left:563px">There are many variations</h2>
    <p style="left:567px">On the other hand, we denounce with righteous indignation and dislike men who are so beguiled and demoralized by the charms of pleasure of the moment, so blinded by desire, that they cannot foresee the pain and trouble that are bound to ensue; and equal blame belongs to those who fail in their duty through</p>
    <div class="btn-orange" style="left:562px;top:944px;width:144px;height:44px;font-size:20px">Read more</div>
  </article>

  <aside class="blog">
    <h3>Latest Blog Post</h3>
    <div class="heart" style="top:690px;background:#e4e4e4" role="img" aria-label="Sketched grey heart"></div>
    <div class="post-title" style="top:703px">On the other hand</div>
    <div class="post-date" style="top:727px">Jul 27, 2011</div>
    <div class="heart" style="top:793px;background:#d9262c" role="img" aria-label="Red heart with pencil"></div>
    <div class="post-title" style="top:792px">With righteous indignation like</div>
    <div class="post-date" style="top:834px">Jul 27, 2011</div>
    <div class="heart" style="top:896px;background:#e4e4e4" role="img" aria-label="Sketched grey heart"></div>
    <div class="post-title" style="top:897px">Choice is untrammelled</div>
    <div class="post-date" style="top:939px">Jul 27, 2011</div>
    <div class="more-posts"><span style="color:#333">›</span> View more Blog Posts</div>
  </aside>

  <footer class="footer">
    <h4 style="left:191px">Read more</h4>
    <ul class="links">
      <li style="top:48px">Why zMatchy</li>
      <li style="top:73px">How it works</li>
      <li style="top:101px">Sign Up</li>
      <li style="top:131px">Login</li>
      <li style="top:158px">About Us</li>
    </ul>
    <div class="abs" style="left:197px;top:212px;font-size:11px">© 2011 by zMatchy.net All Rights Reserved.</div>

    <h4 style="left:468px">Let's Talk</h4>
    <div class="ffield" style="left:465px;top:53px;width:192px;height:35px">Name</div>
    <div class="ffield" style="left:674px;top:53px;width:192px;height:35px">E-mail Address</div>
    <div class="ffield" style="left:466px;top:97px;width:401px;height:101px">Comment</div>
    <div class="send">Send Message</div>

    <h4 style="left:1001px">Social media</h4>
    <div class="chip" style="left:1001px;top:53px;width:52px;height:22px;font-size:11px;color:#3d5a98">Like</div>
    <div class="abs" style="left:1063px;top:59px;width:11px;height:11px;background:#3d5a98"></div>
    <div class="abs" style="left:1086px;top:59px;font-size:11px;font-weight:700">3123 peoples</div>
    <div class="chip" style="left:1002px;top:92px;width:77px;height:26px;font-size:15px;color:#2a8fc7;font-weight:700">Chirp</div>
    <div class="chip" style="left:1085px;top:92px;width:52px;height:26px;font-size:14px;color:#2a8fc7">7,231</div>
    <div class="chip" style="left:1002px;top:139px;width:31px;height:19px;font-size:11px;color:#1a5bbf;font-weight:700">+1</div>
    <div class="chip" style="left:1040px;top:139px;width:38px;height:19px;font-size:11px;background:#2c2c2c;color:#fff;border-color:#444">13k</div>
  </footer>

</div>
</body>
</html>
```